Electrical Business Card Design

New electrical business targeting my local area
Installations
Repairs
Switchboards
TV / Vistacast / Antennas
Telephone
Data Networks
Audio Visual
Licence # 518247K
ABN 63918257041
I would like some white background, black writing, red, blue & green can be used
Designer discretion to be used on layout, colour placement & any images
Updates
Project Deadline Extended
Reason: To give designers more time, I thought 5 days wasn't enough
Please don't just create generic business cards................include personal details e.g. business name, contact name, ph #, email. Also include the things I do, licence # & abn (refer to brief for all details)
Thanks
Project Deadline Extended
Reason: Would like more designs & have now committed my payment, thank you
Industry/Entity Type
Electrical
Contact Information for Business Card
Korvale Electrical Services,
Derek Halloran,
0498 351 672,
korvaleelectrical@plumnet.net.au,
My suburb is Ryde
Look and feel

```html
<!DOCTYPE html>
<html lang="en">
<head>
<meta charset="utf-8">
<title>Korvale Electrical Services – Business Card</title>
<link rel="stylesheet" href="https://fonts.googleapis.com/css2?family=Tinos&display=swap">
<style>
  :root {
    --ink: #000000;
    --accent-cyan: #00f0f0;
    --accent-red: #ff0000;
    --paper: #ffffff;
  }
  * { margin: 0; padding: 0; box-sizing: border-box; }
  html, body {
    width: 1200px;
    height: 900px;
    overflow: hidden;
    background: var(--paper);
  }
  .card {
    position: relative;
    width: 1200px;
    height: 900px;
    overflow: hidden;
    background: var(--paper);
    font-family: "Tinos", "Times New Roman", serif;
    color: var(--ink);
  }
  .line {
    --sx: 0.5;
    position: absolute;
    white-space: nowrap;
    line-height: 1;
    font-weight: 400;
  }
  .centered {
    transform-origin: center;
    transform: translateX(-50%) scaleX(var(--sx));
  }
  .left {
    transform-origin: left center;
    transform: scaleX(var(--sx));
  }

  .owner-name    { left: 380px; top: 45px;  font-size: 100px; --sx: 0.41; }
  .owner-mobile  { left: 380px; top: 160px; font-size: 54px;  --sx: 0.5; }
  .business-name { left: 262px; top: 329px; font-size: 100px; --sx: 0.41; }
  .suburb        { left: 261px; top: 424px; font-size: 100px; --sx: 0.41; }
  .tagline       { left: 261px; top: 528px; font-size: 57px; --sx: 0.5; color: var(--accent-red); }
  .email         { left: 261px; top: 616px; font-size: 57px; --sx: 0.5; color: var(--accent-cyan); }
  .credentials   { left: 261px; top: 701px; font-size: 57px; --sx: 0.48; }
  .credentials .gap { display: inline-block; width: 80px; }

  .services-title { left: 703px; top: 122px; font-size: 106px; --sx: 0.4; }

  .services { list-style: none; }
  .service {
    position: absolute;
    left: 703px;
    font-size: 60px;
    --sx: 0.48;
    display: flex;
    align-items: center;
  }
  .service::before {
    content: "";
    display: inline-block;
    width: 28px;
    height: 20px;
    border-radius: 50%;
    background: currentColor;
    margin-right: 66px;
  }
  .service--alt { color: var(--accent-cyan); }
  .service:nth-child(1) { top: 263px; }
  .service:nth-child(2) { top: 351px; }
  .service:nth-child(3) { top: 439px; }
  .service:nth-child(4) { top: 533px; }
  .service:nth-child(5) { top: 619px; }
  .service:nth-child(6) { top: 705px; }
</style>
</head>
<body>
  <main class="card">
    <section class="contact">
      <h1 class="line centered owner-name">Derek Halloran</h1>
      <p class="line centered owner-mobile">Mobile #&nbsp; 0498 351 672</p>
      <h2 class="line centered business-name">Korvale Electrical Services</h2>
      <p class="line centered suburb">Ryde</p>
      <p class="line centered tagline">Reliable, Honest</p>
      <p class="line centered email">email: korvale@plumnet.net.au</p>
      <p class="line centered credentials">Licence # 518247K<span class="gap"></span>ABN&nbsp; 63918257041</p>
    </section>

    <section class="offerings">
      <h2 class="line left services-title">Things I Do</h2>
      <ul class="services">
        <li class="line left service">New Installations</li>
        <li class="line left service service--alt">Repairs and Additions</li>
        <li class="line left service">TV/Vistacast/Antennas</li>
        <li class="line left service service--alt">Phones</li>
        <li class="line left service">Data Networks</li>
        <li class="line left service service--alt">Audio Visual</li>
      </ul>
    </section>
  </main>
</body>
</html>
```